Vantrel

I already have a website created through Plovix.com - https://vantrel.co.nz.

Its an accounting services business, can get ideas from tzhl.co.nz, fwu.co.nz, yrx.co.nz

I would like to have this recreated using coding. I need the following features and functionalities incorporated:

- Live Chat feature
- Moving Carousel feature for Reviews
- Advanced SEO support (Google Analytics)

Industry/Entity Type

accounting

Coding

Coded - Design and coding required

Number of Pages Required

5+ page

```html
<!DOCTYPE html>
<html lang="en">
<head>
<meta charset="utf-8">
<title>Vantrel — Accounting Services</title>
<link href="https://fonts.googleapis.com/css2?family=Lexend:wght@400;500;600&family=Poppins:ital,wght@0,400;0,500;0,600;1,400&display=swap" rel="stylesheet">
<style>
:root{
  --dark:#3e4e4a;
  --dark-line:#5d726d;
  --teal:#a3d9c9;
  --teal-deep:#7cc2ad;
  --ink:#2c3a37;
  --muted:#555f5c;
  --light:#eceeef;
  --white:#ffffff;
  --field:#e4e7e6;
}
*{margin:0;padding:0;box-sizing:border-box}
html,body{width:1200px;height:5141px;overflow:hidden}
body{position:relative;font-family:"Poppins",sans-serif;color:var(--ink);background:var(--white)}
.abs{position:absolute}
.heading{font-family:"Lexend",sans-serif;font-weight:500;letter-spacing:-0.5px;line-height:1.1}
.eyebrow{font-size:15px;color:var(--teal-deep);letter-spacing:0.5px;text-transform:uppercase}
.rule{position:absolute;width:74px;height:2px;background:var(--teal-deep)}
.rule::after{content:"";position:absolute;left:31px;top:-4px;width:10px;height:10px;border-radius:50%;background:var(--teal-deep)}
.btn{position:absolute;display:flex;align-items:center;border-radius:40px;font-family:"Poppins",sans-serif;font-weight:500;text-transform:uppercase}
.btn .arrow{position:absolute;right:6px;top:50%;transform:translateY(-50%);border-radius:50%;border:2px solid currentColor;display:flex;align-items:center;justify-content:center}
.photo{position:absolute}

/* header */
.site-header{left:0;top:0;width:1200px;height:120px;background:var(--dark);color:var(--white)}
.topline{font-size:14px;display:flex;align-items:center;gap:10px}
.nav{font-size:13px;font-weight:500;display:flex;gap:30px;text-transform:uppercase}
.nav .active{color:var(--teal)}
.logo-disc{left:490px;top:-110px;width:220px;height:310px;border-radius:0 0 110px 110px;background:var(--dark)}
.logo-name{font-family:"Lexend",sans-serif;font-weight:500;color:var(--teal);letter-spacing:5px;text-transform:uppercase}

/* hero */
.hero-title{right:60px;top:292px;width:480px;text-align:center;font-size:52px;color:var(--ink)}

/* about */
.about-text{left:122px;top:1154px;width:444px;font-size:13px;line-height:27px;color:var(--muted)}

/* services */
.services{left:0;top:1490px;width:1200px;height:992px;background:var(--dark);color:var(--white)}
.card{position:absolute;width:343px;height:270px;border:2px solid var(--dark-line)}
.card .icon{position:absolute;left:40px;top:-48px;width:96px;height:96px;background:var(--teal);display:flex;align-items:center;justify-content:center}
.card h3{position:absolute;left:26px;top:54px;font-family:"Poppins",sans-serif;font-weight:500;font-size:25px;color:var(--teal)}
.card p{position:absolute;left:26px;top:98px;width:290px;font-size:13.5px;line-height:20px;text-align:justify;color:#d8dedc}
.card .more{position:absolute;left:26px;top:222px;font-size:12.5px;text-decoration:underline;color:#d8dedc;text-transform:uppercase}

/* testimonials */
.tcard{position:absolute;top:2760px;width:344px;height:152px;background:var(--white);box-shadow:0 4px 16px rgba(0,0,0,0.1)}
.tcard .quote{position:absolute;left:28px;top:-18px;font-family:"Lexend",sans-serif;font-weight:600;font-size:96px;line-height:1;color:var(--dark)}
.tcard p{position:absolute;left:30px;top:30px;width:284px;font-size:14px;font-style:italic;line-height:26px;text-align:justify;text-align-last:center;color:var(--muted)}
.person{position:absolute;top:2934px;display:flex;align-items:center;gap:16px}
.person .avatar{width:62px;height:62px;border-radius:50%;background:linear-gradient(135deg,#c9c3bd,#8b817a)}
.person strong{display:block;font-weight:500;font-size:18px;color:var(--ink);line-height:1.2}
.person span{display:block;font-size:12px;color:var(--muted)}
.person em{font-style:normal;color:#f2c21b;font-size:12px;letter-spacing:1px}

/* cta */
.cta{left:0;top:3245px;width:1200px;height:627px}
.cta-title{left:70px;top:3350px;font-size:62px;color:var(--white);text-transform:uppercase;line-height:78px}

/* contact */
.field{position:absolute;background:var(--white);box-shadow:0 2px 10px rgba(0,0,0,0.12);font-size:12px;color:#9aa3a0;padding:12px 20px}

/* footer */
.site-footer{left:0;top:4662px;width:1200px;height:479px;background:var(--dark);color:var(--white)}
.finfo{position:absolute;top:4935px;display:flex;align-items:center;gap:14px;font-size:12.5px;line-height:17px}
.finfo .ico{width:34px;height:34px;background:var(--teal);border-radius:4px;display:flex;align-items:center;justify-content:center}
.flinks{left:0;top:5036px;width:1200px;display:flex;justify-content:center;gap:38px;font-size:12.5px;text-transform:uppercase}
.social{position:absolute;top:5104px;width:26px;height:26px;background:var(--teal);border-radius:3px}
</style>
</head>
<body>

<!-- Header -->
<header class="site-header abs">
  <div class="topline abs" style="left:68px;top:22px">
    <svg width="18" height="18" viewBox="0 0 24 24"><path d="M6.6 10.8a15 15 0 006.6 6.6l2.2-2.2a1 1 0 011-.25 11.4 11.4 0 003.6.6 1 1 0 011 1V20a1 1 0 01-1 1A17 17 0 013 4a1 1 0 011-1h3.5a1 1 0 011 1c0 1.25.2 2.45.6 3.6a1 1 0 01-.25 1z" fill="#fff"/></svg>
    <span>021480372</span>
  </div>
  <div class="topline abs" style="right:66px;top:22px">
    <svg width="20" height="15" viewBox="0 0 20 15"><rect x="1" y="1" width="18" height="13" fill="none" stroke="var(--teal)" stroke-width="2"/><path d="M1 1l9 7 9-7" fill="none" stroke="var(--teal)" stroke-width="2"/></svg>
    <span>contact@vantrel.co.nz</span>
  </div>
  <nav class="nav abs" style="left:66px;top:73px"><span class="active">Home</span><span>About Us</span><span>Services</span></nav>
  <nav class="nav abs" style="right:76px;top:73px"><span>Pricing</span><span>Live Chat Feature</span><span>Contact Us</span></nav>
</header>
<div class="logo-disc abs"></div>
<div class="abs" style="left:582px;top:34px;width:36px;height:36px;border-radius:50%;background:var(--teal)"></div>
<div class="logo-name abs" style="left:490px;top:124px;width:220px;text-align:center;font-size:24px">Vantrel</div>

<!-- Hero -->
<section>
  <div class="photo" role="img" aria-label="Hands holding a tablet showing business charts" style="left:0;top:120px;width:1200px;height:678px;background:linear-gradient(90deg,#2e4a66 0%,#5f7d96 25%,#b9c6d0 45%,#e4e6e8 62%,#e9eaeb 100%)"></div>
  <h1 class="heading hero-title abs">We Empower Businesses Ledgra Certified, Results Driven</h1>
  <div class="btn" style="left:785px;top:578px;width:266px;height:74px;background:var(--dark);color:var(--white);font-size:22px;padding-left:34px;text-transform:uppercase">Get Started
    <span class="arrow" style="width:58px;height:58px"><svg width="24" height="24" viewBox="0 0 24 24"><path d="M6 18L18 6M9 6h9v9" fill="none" stroke="#fff" stroke-width="2.4"/></svg></span>
  </div>
</section>

<!-- About -->
<section>
  <div class="eyebrow abs" style="left:126px;top:938px">Who We Are</div>
  <h2 class="heading abs" style="left:122px;top:958px;font-size:52px;text-transform:uppercase">About Us</h2>
  <div class="rule" style="left:124px;top:1030px"></div>
  <h3 class="abs" style="left:122px;top:1066px;font-family:'Lexend',sans-serif;font-weight:500;font-size:32px;color:var(--dark)">I am Maryam</h3>
  <div class="abs" style="left:122px;top:1112px;font-size:14px;font-weight:500;color:var(--dark)">BCom, GradDip, CA</div>
  <p class="about-text abs">A Chartered Accountant with in-depth professional experience across New Zealand's diverse financial landscape. Throughout my career I have had the privilege of working across various sectors, including commercial organisations, charitable trusts and for purpose organisations, government-funded entities, as well as the health, disability, and education sectors.</p>
  <div class="btn" style="left:118px;top:1340px;width:176px;height:48px;background:var(--dark);color:var(--white);font-size:14px;padding-left:24px">Read More
    <span class="arrow" style="width:38px;height:38px"><svg width="16" height="16" viewBox="0 0 24 24"><path d="M6 18L18 6M9 6h9v9" fill="none" stroke="#fff" stroke-width="2.6"/></svg></span>
  </div>
  <div class="abs" style="left:620px;top:864px;width:128px;height:128px;border-radius:50%;background:var(--teal)"></div>
  <div class="abs" style="left:880px;top:1243px;width:150px;height:150px;border-radius:50%;background:#e2e4e4"></div>
  <div class="photo" role="img" aria-label="Portrait of the accountant seated on a doorstep" style="left:625px;top:960px;width:420px;height:420px;border-radius:50%;background:linear-gradient(160deg,#8a8f93,#3a3d42 55%,#6b5a4a)"></div>
</section>

<!-- Services -->
<section class="services abs">
  <div class="abs" style="left:106px;top:178px;font-size:16px;text-transform:uppercase;color:#d8dedc">What We Do</div>
  <h2 class="heading abs" style="left:104px;top:206px;font-size:56px;line-height:62px;text-transform:uppercase">Our<br>Services</h2>
  <div class="rule" style="left:106px;top:347px;background:#d8dedc"></div>
</section>
<div class="card" style="left:430px;top:1622px">
  <div class="icon"><svg width="52" height="52" viewBox="0 0 52 52" fill="none" stroke="#3e4e4a" stroke-width="2.4"><rect x="10" y="6" width="26" height="34"/><path d="M16 14h14M16 20h14M16 26h8"/><circle cx="36" cy="36" r="9"/><path d="M36 31v10M33 34h5M33 38h5"/></svg></div>
  <h3>Monthly Reporting</h3>
  <p>Lorem ipsum dolor sit amet, consectetur adipiscing elit, sed do eiusmod tempor incididunt ut labore et dolore magna aliqua. Ut enim ad minim veniam, quis nostrud exercitation ullamco.</p>
  <span class="more">Read More</span>
</div>
<div class="card" style="left:792px;top:1622px">
  <div class="icon"><svg width="52" height="52" viewBox="0 0 52 52" fill="#3e4e4a"><rect x="10" y="30" width="7" height="14"/><rect x="21" y="24" width="7" height="20"/><rect x="32" y="18" width="7" height="26"/><path d="M10 24l11-8 8 5 12-11" fill="none" stroke="#3e4e4a" stroke-width="3"/><path d="M35 8h8v8z"/></svg></div>
  <h3>Cash Flow Reporting</h3>
  <p>Lorem ipsum dolor sit amet, consectetur adipiscing elit, sed do eiusmod tempor incididunt ut labore et dolore magna aliqua. Ut enim ad minim veniam, quis nostrud exercitation ullamco.</p>
  <span class="more">Read More</span>
</div>
<div class="card" style="left:68px;top:1982px">
  <div class="icon"><svg width="52" height="52" viewBox="0 0 52 52" fill="#3e4e4a"><circle cx="14" cy="14" r="5"/><circle cx="26" cy="12" r="6"/><circle cx="38" cy="14" r="5"/><path d="M6 28a8 8 0 0116 0zM30 28a8 8 0 0116 0zM17 26a9 9 0 0118 0z"/><circle cx="26" cy="38" r="9" fill="none" stroke="#3e4e4a" stroke-width="2.6"/><path d="M26 33v10" stroke="#3e4e4a" stroke-width="2"/></svg></div>
  <h3>Budgets &amp; Forecasts</h3>
  <p>Lorem ipsum dolor sit amet, consectetur adipiscing elit, sed do eiusmod tempor incididunt ut labore et dolore magna aliqua. Ut enim ad minim veniam, quis nostrud exercitation ullamco.</p>
  <span class="more">Read More</span>
</div>
<div class="card" style="left:430px;top:1982px">
  <div class="icon"><svg width="52" height="52" viewBox="0 0 52 52"><circle cx="26" cy="26" r="18" fill="#3e4e4a"/><path d="M19 33l14-14" stroke="#a3d9c9" stroke-width="3"/><circle cx="20" cy="20" r="3.5" fill="#a3d9c9"/><circle cx="32" cy="32" r="3.5" fill="#a3d9c9"/></svg></div>
  <h3>GST, PAYE</h3>
  <p>Lorem ipsum dolor sit amet, consectetur adipiscing elit, sed do eiusmod tempor incididunt ut labore et dolore magna aliqua. Ut enim ad minim veniam, quis nostrud exercitation ullamco.</p>
  <span class="more">Read More</span>
</div>
<div class="card" style="left:792px;top:1982px">
  <div class="icon"><svg width="52" height="52" viewBox="0 0 52 52" fill="none" stroke="#3e4e4a" stroke-width="2.4"><rect x="22" y="6" width="22" height="14"/><circle cx="33" cy="13" r="3"/><path d="M6 30h10l8 4h10a3 3 0 010 6H22M6 44h24l14-8"/></svg></div>
  <h3>Payroll</h3>
  <p>Lorem ipsum dolor sit amet, consectetur adipiscing elit, sed do eiusmod tempor incididunt ut labore et dolore magna aliqua. Ut enim ad minim veniam, quis nostrud exercitation ullamco.</p>
  <span class="more">Read More</span>
</div>
<div class="btn" style="left:466px;top:2263px;width:268px;height:72px;border:2px solid var(--white);color:var(--white);font-size:22px;padding-left:44px">View More
  <span class="arrow" style="width:58px;height:58px"><svg width="24" height="24" viewBox="0 0 24 24"><path d="M6 18L18 6M9 6h9v9" fill="none" stroke="#fff" stroke-width="2.4"/></svg></span>
</div>

<!-- Testimonials -->
<section>
  <div class="eyebrow abs" style="left:0;top:2586px;width:1200px;text-align:center">Reviews</div>
  <h2 class="heading abs" style="left:0;top:2606px;width:1200px;text-align:center;font-size:52px;text-transform:uppercase">Our Testimonials</h2>
  <div class="rule" style="left:563px;top:2680px"></div>
  <div class="tcard" style="left:66px"><span class="quote">“</span><p>Lorem ipsum dolor sit amet, conse ctetuer adipiscing elit. Aenean comodo ligula eget dolor. Aenean massa. Cum sociis natoque pen atibus et magnis</p></div>
  <div class="tcard" style="left:428px"><span class="quote">“</span><p>Lorem ipsum dolor sit amet, conse ctetuer adipiscing elit. Aenean comodo ligula eget dolor. Aenean massa. Cum sociis natoque pen atibus et magnis</p></div>
  <div class="tcard" style="left:790px"><span class="quote">“</span><p>Lorem ipsum dolor sit amet, conse ctetuer adipiscing elit. Aenean comodo ligula eget dolor. Aenean massa. Cum sociis natoque pen atibus et magnis</p></div>
  <div class="person" style="left:132px"><div class="avatar" role="img" aria-label="Reviewer portrait"></div><div><strong>Corin Walsh</strong><span>Managing Director</span><em>★★★★★</em></div></div>
  <div class="person" style="left:494px"><div class="avatar" role="img" aria-label="Reviewer portrait"></div><div><strong>Tavish Orme</strong><span>Managing Director</span><em>★★★★★</em></div></div>
  <div class="person" style="left:856px"><div class="avatar" role="img" aria-label="Reviewer portrait"></div><div><strong>Rowan Pike</strong><span>Managing Director</span><em>★★★★★</em></div></div>
  <div class="abs" style="left:542px;top:3074px;width:52px;height:52px;border-radius:50%;background:var(--white);box-shadow:0 3px 10px rgba(0,0,0,0.15);display:flex;align-items:center;justify-content:center"><svg width="20" height="14" viewBox="0 0 20 14"><path d="M19 7H2M7 1L1 7l6 6" fill="none" stroke="#2c3a37" stroke-width="2"/></svg></div>
  <div class="abs" style="left:606px;top:3074px;width:52px;height:52px;border-radius:50%;background:var(--dark);display:flex;align-items:center;justify-content:center"><svg width="20" height="14" viewBox="0 0 20 14"><path d="M1 7h17M13 1l6 6-6 6" fill="none" stroke="#fff" stroke-width="2"/></svg></div>
</section>

<!-- Call to action -->
<section>
  <div class="cta photo" role="img" aria-label="Team members reviewing printed financial charts at a desk" style="background:linear-gradient(90deg,#3e4e4a 0%,#3e4e4a 38%,rgba(62,78,74,0.85) 55%,#6f7d78 75%,#a9a592 100%)"></div>
  <h2 class="heading cta-title abs">Let’s Talk About<br>What Matters<br>To You</h2>
  <p class="abs" style="left:70px;top:3594px;width:560px;font-size:13px;line-height:26px;color:var(--white)">Our value-based pricing is about building trust and delivering results. If you're ready for an accounting partner who sees the bigger picture and values your success, let's chat.</p>
  <div class="btn" style="left:70px;top:3700px;width:350px;height:72px;background:var(--teal);color:var(--dark);font-size:22px;padding-left:28px">Contact Us Today
    <span class="arrow" style="width:58px;height:58px"><svg width="24" height="24" viewBox="0 0 24 24"><path d="M6 18L18 6M9 6h9v9" fill="none" stroke="#3e4e4a" stroke-width="2.4"/></svg></span>
  </div>
</section>

<!-- Contact -->
<section>
  <div class="abs" style="left:120px;top:3994px;width:128px;height:128px;border-radius:50%;background:var(--teal)"></div>
  <div class="abs" style="left:108px;top:4406px;width:156px;height:156px;border-radius:50%;background:#e2e4e4"></div>
  <div class="photo" role="img" aria-label="Hands working over a tablet and documents at a meeting" style="left:123px;top:4095px;width:420px;height:420px;border-radius:50%;background:linear-gradient(140deg,#2f3e5c,#a9aeb8 50%,#e2dcd3)"></div>
  <div class="eyebrow abs" style="left:632px;top:4012px">Get In Touch With</div>
  <h2 class="heading abs" style="left:630px;top:4032px;font-size:52px;text-transform:uppercase">Contact Us</h2>
  <div class="rule" style="left:632px;top:4104px"></div>
  <div class="field" style="left:630px;top:4170px;width:222px;height:42px">First Name:</div>
  <div class="field" style="left:870px;top:4170px;width:222px;height:42px">Last Name:</div>
  <div class="field" style="left:630px;top:4235px;width:222px;height:42px">Phone:</div>
  <div class="field" style="left:870px;top:4235px;width:222px;height:42px">Email:</div>
  <div class="field" style="left:630px;top:4300px;width:462px;height:140px">Mesage:</div>
  <div class="btn" style="left:632px;top:4470px;width:176px;height:52px;background:var(--dark);color:var(--white);font-size:15px;padding-left:38px">Submit
    <span class="arrow" style="width:40px;height:40px"><svg width="16" height="16" viewBox="0 0 24 24"><path d="M6 18L18 6M9 6h9v9" fill="none" stroke="#fff" stroke-width="2.6"/></svg></span>
  </div>
</section>

<!-- Footer -->
<footer class="site-footer abs">
  <div class="abs" style="left:582px;top:84px;width:36px;height:36px;border-radius:50%;background:var(--teal)"></div>
  <div class="logo-name abs" style="left:0;top:170px;width:1200px;text-align:center;font-size:26px">Vantrel</div>
  <div class="abs" style="left:70px;top:346px;width:1066px;height:1px;background:var(--dark-line)"></div>
  <div class="abs" style="left:70px;top:418px;width:1066px;height:1px;background:var(--dark-line)"></div>
  <div class="abs" style="left:66px;top:449px;font-size:11px">Copyright © 2025 All Rights Reserved By Company name</div>
</footer>
<div class="finfo" style="left:228px">
  <span class="ico"><svg width="18" height="18" viewBox="0 0 24 24"><path d="M6.6 10.8a15 15 0 006.6 6.6l2.2-2.2a1 1 0 011-.25 11.4 11.4 0 003.6.6 1 1 0 011 1V20a1 1 0 01-1 1A17 17 0 013 4a1 1 0 011-1h3.5a1 1 0 011 1c0 1.25.2 2.45.6 3.6a1 1 0 01-.25 1z" fill="#3e4e4a"/></svg></span>
  <div>CALL US<br>021480372</div>
</div>
<div class="finfo" style="left:452px">
  <span class="ico"><svg width="20" height="15" viewBox="0 0 20 15"><rect x="1" y="1" width="18" height="13" fill="none" stroke="#3e4e4a" stroke-width="2"/><path d="M1 1l9 7 9-7" fill="none" stroke="#3e4e4a" stroke-width="2"/></svg></span>
  <div>EMAIL US<br>contact@vantrel.co.nz</div>
</div>
<div class="finfo" style="left:760px">
  <span class="ico"><svg width="16" height="20" viewBox="0 0 16 20"><path d="M8 1a7 7 0 00-7 7c0 5 7 11 7 11s7-6 7-11a7 7 0 00-7-7z" fill="#3e4e4a"/><circle cx="8" cy="8" r="2.5" fill="#a3d9c9"/></svg></span>
  <div>Address line Dummy here<br>Address line dummy</div>
</div>
<nav class="flinks abs" style="color:var(--white)">
  <span>About Us</span><span>|</span><span>Services</span><span>|</span><span>Pricing</span><span>|</span><span>Live Chat Feature</span><span>|</span><span>Contact Us</span>
</nav>
<div class="social" style="left:1016px"></div>
<div class="social" style="left:1047px"></div>
<div class="social" style="left:1078px"></div>
<div class="social" style="left:1109px"></div>

</body>
</html>
```